Commercial Real Estate

We need a business card design for a new commercial real estate business that specializes in apartment building brokerage. Not individual units but the entire complex. We find and represent the owners existing buildings and well as new buyers for those buildings. The design should convey trust, integrity, knowledge and growth. It should be easily read.

Target Market(s)

40 to 65 years old

Industry/Entity Type

Real Estate

```html
<!DOCTYPE html>
<html lang="en">
<head>
<meta charset="utf-8">
<title>Halden Property Investments – Business Card</title>
<link rel="stylesheet" href="https://fonts.googleapis.com/css2?family=Arimo:wght@400;700&display=swap">
<style>
  :root {
    --stage: #2b2b2c;
    --card: #ffffff;
    --teal: #6cc6c4;
    --ink: #55595c;
    --rule: #9a9ea1;
  }
  * { box-sizing: border-box; margin: 0; padding: 0; }
  html, body { width: 1200px; height: 900px; overflow: hidden; }
  body {
    background: var(--stage);
    font-family: "Arimo", Arial, sans-serif;
    position: relative;
  }
  .card {
    position: absolute;
    width: 560px;
    height: 320px;
    background: var(--card);
    box-shadow: 0 10px 30px rgba(0,0,0,.45);
  }
  .card--front { left: 320px; top: 80px; }
  .card--back  { left: 320px; top: 480px; }

  /* front */
  .front-brand {
    position: absolute; inset: 0;
    display: flex; flex-direction: column;
    align-items: center; justify-content: center; gap: 14px;
  }
  .brand-mark { width: 26px; height: 26px; background: var(--teal); }
  .brand-name {
    color: var(--ink); font-weight: 700; font-size: 30px;
    letter-spacing: 1px; text-align: center; line-height: 1.25;
  }

  /* back */
  .back-brand {
    position: absolute; left: 34px; top: 0; bottom: 0; width: 180px;
    display: flex; flex-direction: column; align-items: center;
    justify-content: center; gap: 10px;
  }
  .back-brand .brand-mark { width: 18px; height: 18px; }
  .back-brand .brand-name { font-size: 18px; }
  .details {
    position: absolute; left: 240px; top: 58px;
    border-left: 1px solid var(--rule);
    padding-left: 14px; padding-bottom: 8px;
  }
  .person-name {
    color: var(--teal); font-weight: 700; font-size: 19px;
    letter-spacing: 1px; margin-bottom: 12px;
  }
  .contact-list { list-style: none; color: var(--ink); font-size: 13px; }
  .contact-list li { display: flex; align-items: center; gap: 8px; line-height: 18px; }
  .contact-icon { width: 11px; height: 11px; flex: none; }
  .address { margin-top: 22px; color: var(--ink); font-size: 13px; line-height: 17px; }
  .address-label { color: var(--teal); }
</style>
</head>
<body>
  <section class="card card--front" aria-label="Card front">
    <div class="front-brand">
      <span class="brand-mark"></span>
      <p class="brand-name">Halden<br>Property Investments</p>
    </div>
  </section>

  <section class="card card--back" aria-label="Card back">
    <div class="back-brand">
      <span class="brand-mark"></span>
      <p class="brand-name">Halden<br>Property Investments</p>
    </div>
    <div class="details">
      <h1 class="person-name">MARCUS HALE</h1>
      <ul class="contact-list">
        <li>
          <svg class="contact-icon" viewBox="0 0 12 12" aria-hidden="true"><rect width="12" height="12" rx="2" fill="var(--ink)"/><path d="M3.5 2.5h1.5l.7 2-1 .8a5 5 0 0 0 2 2l.8-1 2 .7v1.5c0 .5-.5 1-1 1A6.5 6.5 0 0 1 2.5 3.5c0-.5.5-1 1-1z" fill="#fff"/></svg>
          XXX.XXX.XXX
        </li>
        <li>
          <svg class="contact-icon" viewBox="0 0 12 12" aria-hidden="true"><rect width="12" height="12" rx="2" fill="var(--ink)"/><path d="M2.5 3.5h7v5h-7z M2.5 3.5 6 6.5 9.5 3.5" fill="none" stroke="#fff" stroke-width="1"/></svg>
          marcus.hale@haldenmail.com
        </li>
        <li>
          <svg class="contact-icon" viewBox="0 0 12 12" aria-hidden="true"><rect width="12" height="12" rx="2" fill="var(--ink)"/></svg>
          social.example/haldenproperty
        </li>
      </ul>
      <p class="address">
        <span class="address-label">Address:</span><br>
        PO Box XXXX<br>
        Fake Street, Downtown XXXXX
      </p>
    </div>
  </section>
</body>
</html>
```